Firmen Logo und Visitenkarte mit Terminkarte (Rückseite der Visitenkarte)
Zielgruppe
Feinklar ist ein Kosmetik Institut. Zu den angebotenen Dienstleistungen gehören Kosmetik- und Wellness-Behandlungen.
Aufgabenstellung
Entwerfen Sie bitte ein Logo für meine Internetseite, sowie für eine Visitenkarte mit Terminkarte, die modern, exklusiv und hochwertig strukturiert ist.
Auf der Visitenkarte sollte das Logo stehen: feinklar, Kosmetik, Wellness, Ihr nächster Termin: Freies Feld zum eintragen von Datum und Uhrzeit, Sollten sie Ihren Termin nicht einhalten können, bitte ich Sie diesen 24 Stunden vorher abzusagen. Sowie die Adresse.
Kosmetikerin/Krankenschwester

```html
<!DOCTYPE html>
<html lang="de">
<head>
<meta charset="utf-8">
<title>Feinklar – Visitenkarte und Terminkarte</title>
<link rel="stylesheet" href="https://fonts.googleapis.com/css2?family=Barlow:wght@400;500&display=swap">
<style>
  :root {
    --page: #ffffff;
    --card: #ffffff;
    --card-edge: #d6d6d6;
    --ink: #5e5e5e;
    --leaf: #a3cd4a;
    --leaf-soft: #e1efc8;
  }
  * { margin: 0; padding: 0; box-sizing: border-box; }
  html, body {
    width: 846px; height: 1200px; overflow: hidden;
    background: var(--page);
    font-family: "Barlow", Arial, sans-serif;
    color: var(--ink);
  }
  .canvas { position: relative; width: 846px; height: 1200px; }
  .card {
    position: absolute; left: 255px; width: 336px; height: 496px;
    background: var(--card);
    border: 1px solid var(--card-edge);
    text-align: center;
  }
  .card--front { top: 105px; }
  .card--back { top: 640px; }

  .brand { position: absolute; top: 70px; left: 0; right: 0; }
  .brand__name {
    display: inline-flex; align-items: center; gap: 10px;
    font-size: 58px; font-weight: 400; letter-spacing: 1px; line-height: 1;
    color: var(--ink);
  }
  .brand__dot { width: 14px; height: 14px; border-radius: 50%; background: var(--leaf); }
  .brand__tagline {
    margin-top: 12px; font-size: 17px; color: var(--leaf); letter-spacing: 0.3px;
  }

  .contact { position: absolute; top: 312px; left: 0; right: 0; }
  .contact__name { font-size: 17px; color: var(--leaf); }
  .contact__role { font-size: 10px; color: var(--leaf); margin-top: 3px; letter-spacing: 0.3px; }
  .contact__lines { margin-top: 16px; font-size: 15.5px; line-height: 1.35; letter-spacing: 0.3px; }
  .contact__web { color: var(--leaf); }

  .appointment { position: absolute; top: 300px; left: 0; right: 0; }
  .appointment__label { font-size: 15px; letter-spacing: 0.3px; }
  .appointment__field {
    display: block; margin: 10px auto 0; width: 256px; height: 42px;
    background: var(--leaf-soft);
  }
  .notice {
    position: absolute; bottom: 22px; left: 0; right: 0;
    font-size: 9.5px; line-height: 1.4; letter-spacing: 0.2px;
  }
</style>
</head>
<body>
<main class="canvas">
  <section class="card card--front" aria-label="Visitenkarte Vorderseite">
    <header class="brand">
      <div class="brand__name"><span>feinklar</span><span class="brand__dot"></span></div>
      <p class="brand__tagline">kosmetik &amp; wellness</p>
    </header>
    <address class="contact" style="font-style: normal;">
      <p class="contact__name">Lena Vossberg</p>
      <p class="contact__role">Kosmetikerin/Krankenschwester</p>
      <div class="contact__lines">
        <p>Am Lindenhof 12</p>
        <p>48599 Lindewald</p>
        <p>Tel. 01234 567890</p>
        <p>Email: feinklar@hautpflege-mail.example</p>
        <p class="contact__web">www.kosmetik-lindewald.example</p>
      </div>
    </address>
  </section>

  <section class="card card--back" aria-label="Terminkarte Rückseite">
    <header class="brand">
      <div class="brand__name"><span>feinklar</span><span class="brand__dot"></span></div>
      <p class="brand__tagline">kosmetik &amp; wellness</p>
    </header>
    <div class="appointment">
      <p class="appointment__label">Ihr nächster Termin:</p>
      <span class="appointment__field" aria-label="Feld für Datum und Uhrzeit"></span>
    </div>
    <p class="notice">Sollten Sie Ihren Termin nicht einhalten können,<br>bitte ich Sie diesen 24 Stunden vorher abzusagen.</p>
  </section>
</main>
</body>
</html>
```